Letter Head, for use on daily correspondence with other companies

Hi

I want a professional Letter head, That my company can use to corresponded with other companies we do business with on a daily basis.

I want this done as soon as possible as this is peak session for us.

I have attached the company logo so please be creative and professional.
Kind regards

Marcus

Target Market(s)

All Audience searching for tickets, people in the entertainment world

Industry/Entity Type

Entertainment Industry

Font styles to use
Serif
Sans Serif
Decorative
Script

Requirements
Must have
• Very professional image.
• I will know want i want when i see it
• so please do your utmost in your professional standards
• Address of the company 24 hollin lane, telephone number 0207 562 3198
• Vat number: 487 2915 06.
• This letter head my be able to acomodate usage for directors & CEO as well as managers and employess
Nice to have
• A great professional image
Should not have
• Be creative please

```html
<!DOCTYPE html>
<html lang="en">
<head>
<meta charset="utf-8">
<title>Stagepass Letterhead</title>
<link href="https://fonts.googleapis.com/css2?family=PT+Sans:wght@400;700&display=swap" rel="stylesheet">
<style>
  :root {
    --paper: #f2f0eb;
    --red: #e3232c;
    --red-dark: #c81d25;
    --red-deep: #b5171f;
    --red-light: #ec3a40;
    --ink: #1d1d1b;
    --white: #ffffff;
    --social-a: #2a9fd6;
    --social-b: #3b5a98;
  }
  * { margin: 0; padding: 0; box-sizing: border-box; }
  html, body { width: 848px; height: 1200px; overflow: hidden; background: var(--paper); }
  .letterhead {
    position: relative;
    width: 848px;
    height: 1200px;
    background: var(--paper);
    font-family: "PT Sans", Arial, sans-serif;
    color: var(--ink);
    overflow: hidden;
  }
  .header-shape, .footer-shape { position: absolute; left: 0; display: block; }
  .header-shape { top: 0; }
  .footer-shape { bottom: 0; }
  .brand-name {
    position: absolute;
    top: 4px;
    left: 98px;
    font-size: 42px;
    font-weight: 700;
    color: var(--white);
    letter-spacing: -0.5px;
    line-height: 1;
  }
  .letter-body {
    position: absolute;
    top: 249px;
    left: 115px;
    width: 647px;
    font-size: 15px;
    line-height: 21.5px;
    text-align: justify;
    hyphens: auto;
  }
  .letter-body p { margin-bottom: 21.5px; }
  .letter-body .section-break { margin-bottom: 43px; }
  .contact-block {
    position: absolute;
    top: 1104px;
    left: 353px;
    display: grid;
    grid-template-columns: 103px 150px;
    font-size: 7.5px;
    line-height: 9.2px;
    color: var(--white);
  }
  .contact-label { font-weight: 700; color: var(--ink); }
  .social-list {
    position: absolute;
    top: 1116px;
    left: 618px;
    list-style: none;
    font-size: 7px;
    color: var(--white);
  }
  .social-item { display: flex; align-items: center; gap: 7px; height: 24px; }
  .social-dot { width: 16px; height: 16px; border-radius: 50%; background: var(--social-a); }
  .social-item.second .social-dot { background: var(--social-b); }
</style>
</head>
<body>
<div class="letterhead">
  <svg class="header-shape" width="848" height="150" viewBox="0 0 848 150" aria-hidden="true">
    <polygon points="0,0 591,0 0,110" fill="var(--red)"/>
    <polygon points="0,0 250,0 96,36" fill="var(--red-light)"/>
    <polygon points="0,0 96,36 0,146" fill="var(--red-dark)"/>
  </svg>
  <div class="brand-name">stagepass</div>

  <main class="letter-body">
    <p>Dear Mr. Marcus ,</p>
    <p>Lorem ipsum dolor sit amet, consectetur adipiscing elit. Maecenas ac urna ex. Etiam vitae ornare ipsum. Nam at consectetur quam. Curabitur fermentum nisl tortor, sed pharetra ligula convallis rutrum.</p>
    <p>Integer pulvinar dapibus felis, nec efficitur quam eleifend et. Proin varius convallis nisl eget elementum. Integer eget lorem sit amet elit venenatis tempus ut ut nisl. Integer vitae blandit dui, non sodales nisi. Sed rutrum vulputate dolor, imperdiet feugiat nibh facilisis in.</p>
    <p>Proin elementum sapien felis, et tempor nisl lacinia sed. Nulla et sagittis massa, nec dignissim velit. Morbi vestibulum tristique velit ut feugiat. Quisque hendrerit dapibus velit, non varius mauris faucibus ac. Curabitur aliquet congue augue vel imperdiet. Etiam efficitur mi vitae finibus molestie.</p>
    <p class="section-break">Duis imperdiet, augue sit amet convallis posuere, libero purus varius orci, in lacinia neque purus vitae augue. Proin blandit id felis eu interdum. Nulla lorem mauris, tincidunt et tempor ac, viverra viverra sapien. Suspendisse dignissim felis at ipsum fringilla, et gravida leo porttitor.</p>
    <p>Vestibulum semper varius dapibus. Nunc rhoncus neque a felis rutrum consequat. Aenean ac eros sit amet nulla sagittis consequat et eget orci. Nunc id luctus est. Donec eleifend at ante vitae sollicitudin. Donec tristique ultrices purus, ac fermentum augue eleifend vel.</p>
    <p>Morbi non arcu varius, euismod elit a, euismod mi. Phasellus et molestie arcu, ut varius mi. Maecenas dapibus metus nec ornare scelerisque. Vivamus ex odio, pretium in eleifend vel, luctus sit amet urna. Nunc aliquet efficitur sagittis.</p>
  </main>

  <svg class="footer-shape" width="848" height="182" viewBox="0 0 848 182" aria-hidden="true">
    <polygon points="0,28 240,48 712,0 848,28 848,182 0,182" fill="var(--red)"/>
    <polygon points="0,28 240,48 0,110" fill="var(--red-dark)"/>
    <polygon points="712,0 848,28 848,80" fill="var(--red-dark)"/>
    <polygon points="0,110 240,48 500,182 0,182" fill="var(--red-deep)" opacity="0.55"/>
    <polygon points="600,40 848,80 848,182 760,182" fill="var(--red-light)" opacity="0.5"/>
  </svg>

  <footer class="contact-block">
    <span class="contact-label">ADDRESS :</span><span>24 Hollin Lane, N4 3RB</span>
    <span></span><span>London, United Kingdom.</span>
    <span class="contact-label">TELEPHONE NUMBER :</span><span>0207 562 3198</span>
    <span class="contact-label">VAT NUMBER :</span><span>487 2915 06</span>
    <span class="contact-label">WEBSITE :</span><span>www.stagepasstickets.co.uk</span>
  </footer>

  <ul class="social-list">
    <li class="social-item"><span class="social-dot"></span>www.social-one.com/stagepasstickets</li>
    <li class="social-item second"><span class="social-dot"></span>www.social-two.com/stagepasstickets</li>
  </ul>
</div>
</body>
</html>
```